BIX Promotional flyer for students

We're looking for an 8.5" x 11" flyer that will be distributed to schools. Please see language to include in attached files.

Target Market(s)

The parents and teachers of high school students

Industry/Entity Type

Mental health

Other font styles liked:
• Monserrat and Roboto Slab

Requirements
Must have
• See attached pdf for language to be included on the flyer. Please use the color palette from our website: www.bixzone.tv. Please include some imagery of students. Please ensure the
Nice to have
• Feel free to use any of the graphics provided. See our website for our brand look & feel: www.bixzone.tv

```html
<!DOCTYPE html>
<html lang="en">
<head>
<meta charset="utf-8">
<title>BIX Fundraising Flyer</title>
<link href="https://fonts.googleapis.com/css2?family=Bebas+Neue&family=Lexend:wght@300;400;500;600&display=swap" rel="stylesheet">
<style>
  :root {
    --orange: #f07c32;
    --blue: #4f86a8;
    --deep-blue: #5b8fb0;
    --pale-blue: #c9d9e8;
    --teal: #5e9f9e;
    --cream: #f3efe9;
    --ink: #2a2a2a;
    --paper: #ffffff;
    --stage: #e9ecec;
  }
  * { margin: 0; padding: 0; box-sizing: border-box; }
  html, body { width: 800px; height: 1200px; overflow: hidden; background: var(--stage); }
  .flyer {
    position: absolute; left: 0; top: 88px;
    width: 800px; height: 1023px;
    background: var(--paper);
    overflow: hidden;
    font-family: "Lexend", sans-serif;
    color: var(--ink);
  }
  .hero { position: absolute; left: 0; top: 0; width: 800px; height: 426px; background: var(--cream); overflow: hidden; }
  .hero-shapes { position: absolute; left: 0; top: 0; }
  .hero-photo {
    position: absolute; left: 349px; top: 78px; width: 451px; height: 348px;
    background: linear-gradient(160deg, rgba(233,226,218,0.85), rgba(200,185,170,0.85) 55%, rgba(120,130,140,0.8));
    border-top-left-radius: 200px;
  }
  .brand { position: absolute; left: 47px; top: 50px; display: flex; align-items: center; gap: 12px; }
  .brand-dot { width: 60px; height: 60px; border-radius: 50%; background: var(--orange); }
  .brand-name { font-weight: 600; font-size: 68px; color: var(--orange); line-height: 1; }
  .headline { position: absolute; left: 44px; top: 250px; font-family: "Bebas Neue", sans-serif; line-height: 0.9; }
  .headline-top { display: block; font-size: 74px; color: var(--blue); }
  .headline-bottom { display: block; font-size: 98px; color: var(--orange); }
  .band { position: absolute; left: 0; top: 426px; width: 800px; height: 80px; background: var(--orange);
    display: flex; align-items: center; justify-content: center; }
  .band-text { font-weight: 500; font-size: 62px; color: var(--paper); letter-spacing: 0.5px; }
  .subhead { position: absolute; left: 0; width: 800px; top: 504px; text-align: center;
    font-weight: 500; font-size: 51px; color: var(--blue); letter-spacing: 0.5px; }
  .gallery-item { position: absolute; top: 572px; height: 180px; }
  .gallery-item.one { left: 48px; width: 230px; background: linear-gradient(135deg, #d8d4cf, #b6a895 60%, #8fb2ae); }
  .gallery-item.two { left: 300px; width: 216px; background: linear-gradient(135deg, #ece8e2, #cbb8a3 55%, #f2a36f); }
  .gallery-item.three { left: 538px; width: 215px; background: linear-gradient(135deg, #eef0f2, #c5c2bd 55%, #a9cfe0); }
  .intro { position: absolute; left: 48px; top: 780px; font-weight: 500; font-size: 26px; }
  .intro-accent { color: var(--orange); }
  .intro-rest { color: var(--blue); }
  .body-copy { position: absolute; left: 48px; top: 818px; width: 710px; font-weight: 300; font-size: 20.5px; line-height: 27px; }
  .site { position: absolute; left: 0; width: 800px; top: 938px; text-align: center;
    font-weight: 600; font-size: 26px; letter-spacing: 5px; }
  .site-name { color: var(--orange); }
  .footer-bar { position: absolute; left: 37px; top: 980px; width: 739px; height: 43px;
    background: var(--teal); border-radius: 40px 40px 0 0; }
</style>
</head>
<body>
  <main class="flyer">
    <section class="hero">
      <svg class="hero-shapes" width="800" height="426" viewBox="0 0 800 426">
        <circle cx="363" cy="107" r="112" fill="var(--pale-blue)" opacity="0.85"/>
        <circle cx="56" cy="334" r="57" fill="#dde4ea"/>
        <circle cx="529" cy="192" r="142" fill="var(--deep-blue)"/>
        <circle cx="756" cy="201" r="104" fill="var(--orange)" opacity="0.9"/>
        <circle cx="746" cy="22" r="104" fill="var(--teal)"/>
      </svg>
      <div class="hero-photo" role="img" aria-label="Smiling teacher helping a young girl draw at a desk"></div>
      <div class="brand">
        <span class="brand-dot"></span>
        <span class="brand-name">BIX</span>
      </div>
      <h1 class="headline">
        <span class="headline-top">FUNDRAISE</span>
        <span class="headline-bottom">WITH BIX</span>
      </h1>
    </section>

    <div class="band"><span class="band-text">50% OF ALL PROCEEDS</span></div>
    <h2 class="subhead">GO BACK TO YOUR SCHOOL</h2>

    <div class="gallery-item one" role="img" aria-label="Children playing a letter card game on a classroom floor"></div>
    <div class="gallery-item two" role="img" aria-label="Speech therapist working with a young boy"></div>
    <div class="gallery-item three" role="img" aria-label="Teacher leading a speech therapy class"></div>

    <p class="intro"><span class="intro-accent">Support the mental health</span> <span class="intro-rest">of your students...</span></p>
    <p class="body-copy">BIX is a simple and effective way to improve mental health. Your students will learn valuable coping skills and techniques from expert clinicians who analyze real cases and share their insights and advice.</p>

    <p class="site">www.<span class="site-name">BIXZONE</span>.tv</p>
    <div class="footer-bar"></div>
  </main>
</body>
</html>
```